Corlane Homes Website for luxury custom home builder with endless detail

Modern website for luxury custom home builder. Simple and easy for viewers to understand what we do. New company formed by retired custom home builder. Company concept is to simplify the building experience with modern technology and introduce a simple pricing strategy for the client. Website must flow. Prefer page less design or possibly something that is up and coming within the web design community. Two galleries: INTERIOR and EXTERIOR. I would like two click on box's when the website is opened showing the galleries as a centerpiece and would also prefer them to play as a slide show. The page needs to fit the entire screen in size. We would like to use Grey, Black and White or the shade of blue that is in our company logo. I would like to see one of my uploaded photos to be in the background. I would also like a 3rd box that will play some type of animated video describing what we do and what our process is. Hoping this would be more interactive for the viewer than clicking on buttons and navigating around wasting time.

Target Market(s)

affluent buyers ages 30-60 who want to built anything from large estates to downsized luzury homes for the retired crowd.

Industry/Entity Type

Home Builder

Number of Pages Required

1 page

Font styles to use
Sans Serif

Colors
33a6d7
000000
333333
5c5c5c
9d9d9d
d9d9d9

Requirements
Must have
• Logo and name at top of page. I would like a pageless web design that includes two gallery box's (Interior and Exterior photos) side by side on the first page. I would also like a 3rd box that will be a eVideo explaining what we do and how we do it. I want as little text as possible. I would like the background to be of one of my interior photos that will flow best and pop when the page loads.

```html
<!DOCTYPE html>
<html lang="en">
<head>
<meta charset="utf-8">
<title>Corlane Homes</title>
<link href="https://fonts.googleapis.com/css2?family=Lato:wght@400;700&display=swap" rel="stylesheet">
<style>
:root{
  --brand-blue:#1d4f9c;
  --ink:#1a1a1a;
  --text:#5c5c5c;
  --muted:#9d9d9d;
  --line:#d9d9d9;
  --panel:#f3f3f3;
  --white:#ffffff;
  --dark:#111111;
}
*{margin:0;padding:0;box-sizing:border-box}
html,body{width:1200px;height:802px;overflow:hidden;background:var(--white);font-family:'Lato',sans-serif;color:var(--ink)}
.page{position:relative;width:1200px;height:802px}
.sidebar{position:absolute;left:0;top:0;width:286px;height:726px;background:var(--panel);border-right:1px solid var(--line)}
.brand{position:absolute;left:0;top:22px;width:286px;text-align:center}
.brand-mark{display:block;width:46px;height:46px;margin:0 auto;border:2px solid var(--brand-blue)}
.brand-name{display:block;margin-top:8px;font-size:17px;font-weight:700;color:var(--brand-blue);letter-spacing:1px;text-transform:uppercase}
.gallery{position:absolute;left:67px;width:209px}
.gallery-photo{width:209px;height:118px;border:1px solid var(--line)}
.gallery-photo.interior{background:linear-gradient(180deg,#e4e2de 0%,#cfc8bd 60%,#6e5443 100%)}
.gallery-photo.exterior{background:linear-gradient(180deg,#3b6fc4 0%,#b8a896 45%,#8f8a84 75%,#33b7c9 100%)}
.gallery-photo.more{background:linear-gradient(180deg,#e6e4df 0%,#a69b8b 55%,#6a5c4e 100%)}
.gallery-footer{display:flex;justify-content:space-between;align-items:center;margin-top:6px}
.gallery-title{font-size:11.5px;text-transform:uppercase;color:var(--ink)}
.gallery-arrows{display:flex;gap:3px}
.gallery-arrows span{width:14px;height:13px;background:#d0d0d0;display:flex;align-items:center;justify-content:center}
.divider{position:absolute;left:0;width:286px;height:1px;background:var(--line)}
.nav{position:absolute;top:20px;left:536px;display:flex;gap:16px;font-size:11px;letter-spacing:.3px}
.nav a{color:var(--ink);text-decoration:none;text-transform:uppercase}
.utility{position:absolute;top:19px;left:983px;display:flex;gap:26px;font-size:9.5px;letter-spacing:1.5px;color:var(--ink)}
.utility span{display:flex;align-items:center;gap:6px}
.search{position:absolute;top:19px;left:1124px}
.hero{position:absolute;left:285px;top:52px;width:855px;height:382px;background:linear-gradient(110deg,#2a2420 0%,#7d6d60 30%,#cfd6d4 55%,#9fc8c7 75%,#4d6a3c 100%)}
.hero-caption{position:absolute;left:10px;top:318px;color:var(--white)}
.hero-title{font-size:32px;font-weight:400;letter-spacing:-1px;line-height:1}
.hero-sub{font-size:11.5px;margin-top:4px;padding-left:88px}
.hero-arrows{position:absolute;left:789px;top:350px;display:flex;gap:2px}
.hero-arrows span{width:23px;height:20px;background:var(--white);display:flex;align-items:center;justify-content:center}
.video{position:absolute;left:334px;top:471px;width:426px;height:255px;background:linear-gradient(90deg,#1c1c1c,#262626 60%,#181818)}
.video-play{position:absolute;left:521px;top:573px}
.video-controls{position:absolute;left:334px;top:703px;width:426px;height:23px;background:#0c0c0c;display:flex;align-items:center;font-size:7px;color:#ccc}
.about{position:absolute;left:774px;top:470px;width:360px}
.about h2{font-size:21px;font-weight:700;color:var(--brand-blue);letter-spacing:-.3px}
.about p{font-size:12px;line-height:17.6px;color:var(--text);margin:13px 0 0 2px}
.about p+p{margin-top:11px}
.watch-more{display:inline-block;margin:15px 0 0 3px;padding:0 12px;height:32px;line-height:32px;background:var(--line);font-size:12px;color:var(--ink)}
.footer{position:absolute;left:0;top:758px;width:1200px;height:44px;background:var(--panel);text-align:center;line-height:44px;font-size:10.5px;color:var(--ink)}
</style>
</head>
<body>
<div class="page">
  <aside class="sidebar">
    <div class="brand">
      <span class="brand-mark"></span>
      <span class="brand-name">Corlane Homes</span>
    </div>

    <div class="gallery" style="top:126px">
      <div class="gallery-photo interior" role="img" aria-label="Bright dining room with wooden table, upholstered chairs and linear chandelier"></div>
      <div class="gallery-footer"><span class="gallery-title">Interior Design</span>
        <div class="gallery-arrows">
          <span><svg width="5" height="7" viewBox="0 0 5 7"><path d="M4 .5 1 3.5 4 6.5" fill="none" stroke="#fff" stroke-width="1.2"/></svg></span>
          <span><svg width="5" height="7" viewBox="0 0 5 7"><path d="M1 .5 4 3.5 1 6.5" fill="none" stroke="#fff" stroke-width="1.2"/></svg></span>
        </div></div>
    </div>
    <div class="divider" style="top:285px"></div>

    <div class="gallery" style="top:316px">
      <div class="gallery-photo exterior" role="img" aria-label="Patio courtyard with fire pit and turquoise lounge chairs under blue sky"></div>
      <div class="gallery-footer"><span class="gallery-title">Exterior Design</span>
        <div class="gallery-arrows">
          <span><svg width="5" height="7" viewBox="0 0 5 7"><path d="M4 .5 1 3.5 4 6.5" fill="none" stroke="#fff" stroke-width="1.2"/></svg></span>
          <span><svg width="5" height="7" viewBox="0 0 5 7"><path d="M1 .5 4 3.5 1 6.5" fill="none" stroke="#fff" stroke-width="1.2"/></svg></span>
        </div></div>
    </div>
    <div class="divider" style="top:482px"></div>

    <div class="gallery" style="top:509px">
      <div class="gallery-photo more" role="img" aria-label="Covered patio with ceiling fans, wicker seating and dining table"></div>
      <div class="gallery-footer"><span class="gallery-title">More Design</span>
        <div class="gallery-arrows">
          <span><svg width="5" height="7" viewBox="0 0 5 7"><path d="M4 .5 1 3.5 4 6.5" fill="none" stroke="#fff" stroke-width="1.2"/></svg></span>
          <span><svg width="5" height="7" viewBox="0 0 5 7"><path d="M1 .5 4 3.5 1 6.5" fill="none" stroke="#fff" stroke-width="1.2"/></svg></span>
        </div></div>
    </div>
  </aside>

  <nav class="nav">
    <a href="#">About</a><a href="#">Work</a><a href="#">Latest</a><a href="#">Explore</a><a href="#">Awards</a><a href="#">Contact</a>
  </nav>
  <div class="utility">
    <span>FOLLOW <svg width="8" height="5" viewBox="0 0 8 5"><path d="M.5 .5 4 4 7.5 .5" fill="none" stroke="#999"/></svg></span>
    <span>INFO <svg width="8" height="5" viewBox="0 0 8 5"><path d="M.5 .5 4 4 7.5 .5" fill="none" stroke="#999"/></svg></span>
  </div>
  <svg class="search" width="11" height="11" viewBox="0 0 11 11"><circle cx="4.5" cy="4.5" r="3.5" fill="none" stroke="#222" stroke-width="1.2"/><path d="M7 7l3.5 3.5" stroke="#222" stroke-width="1.2"/></svg>

  <section class="hero" role="img" aria-label="Modern living room with white sofas, fireplace and glass wall opening onto a terrace">
    <div class="hero-caption">
      <div class="hero-title">Luxury custom home builder</div>
      <div class="hero-sub">New company formed by retired custom home builder</div>
    </div>
    <div class="hero-arrows">
      <span><svg width="7" height="11" viewBox="0 0 7 11"><path d="M6 1 1.5 5.5 6 10" fill="none" stroke="#000" stroke-width="2"/></svg></span>
      <span><svg width="7" height="11" viewBox="0 0 7 11"><path d="M1 1 5.5 5.5 1 10" fill="none" stroke="#000" stroke-width="2"/></svg></span>
    </div>
  </section>

  <div class="video" role="img" aria-label="Dimmed video frame of a living room with fireplace"></div>
  <svg class="video-play" width="52" height="52" viewBox="0 0 52 52"><circle cx="26" cy="26" r="24" fill="none" stroke="#fff" stroke-width="3"/><path d="M21 16v20l16-10z" fill="#fff"/></svg>
  <div class="video-controls">
    <svg width="40" height="23" viewBox="0 0 40 23"><path d="M13 7v9l8-4.5z" fill="#fff"/><path d="M29 5v13" stroke="#333"/></svg>
    <svg width="160" height="23" viewBox="0 0 160 23"><rect x="2" y="9.5" width="156" height="4" rx="2" fill="#444"/><rect x="2" y="9.5" width="88" height="4" rx="2" fill="#2a86d4"/><circle cx="90" cy="11.5" r="3.5" fill="#111" stroke="#ddd"/></svg>
    <span style="margin-left:80px">15:00 / 88:20</span>
    <svg width="90" height="23" viewBox="0 0 90 23" style="margin-left:4px"><path d="M5 5v13" stroke="#333"/><path d="M10 9h3l4-3v11l-4-3h-3z" fill="#ccc"/><rect x="24" y="9.5" width="44" height="4" rx="2" fill="#2a86d4"/><circle cx="67" cy="11.5" r="3" fill="#111" stroke="#ddd"/><path d="M74 5v13" stroke="#333"/><path d="M80 8h2M80 8v2M88 8h-2M88 8v2M80 16h2M80 16v-2M88 16h-2M88 16v-2" stroke="#ccc"/></svg>
  </div>

  <section class="about">
    <h2>Our Video</h2>
    <p>Neque porro quisquam est qui dolorem ipsum quia dolor sit amet, consectetur, adipisci velit.There is no one who loves pain itself, who seeks after it and wants to have it, simply because it is pain..</p>
    <p>Neque porro quisquam est qui dolorem ipsum quia dolor sit amet, consectetur, adipisci velit.There is no one who loves pain itself, who seeks after it and wants to have it, simply because it is pain..</p>
    <a class="watch-more">Watch More</a>
  </section>

  <footer class="footer">Corlane homes @ Copyright 2015, All rights reserved.</footer>
</div>
</body>
</html>
```